Company PowerPoint Presentation Template

I am looking for a business powerpoint template tailored to my company that specializes in permafrost services for the mining, transportation, and oil & gas industries. The template would be used to present project findings from studies completed for our clients. I am looking for a crisp, technical, professional business look to the template. Our business is located in North America and English is the primary language used to communicate our work. Complimentary colors associated with the business is blue (RGB, 0,112,192) or something similar in color.

```html
<!DOCTYPE html>
<html lang="en">
<head>
<meta charset="utf-8">
<title>Tundraline Ground Consulting – Presentation Template</title>
<link href="https://fonts.googleapis.com/css2?family=Montserrat:wght@400;500;700;800&display=swap" rel="stylesheet">
<style>
  :root{
    --page:#dcdadb;
    --paper:#ffffff;
    --ink:#1a1d24;
    --brand-blue:#0b6fc2;
    --photo-blue:#3d7db5;
    --rule-grey:#e3e3e3;
    --navy:#0d3d78;
    --muted:#4a4f57;
    --white:#ffffff;
  }
  *{box-sizing:border-box;margin:0;padding:0}
  html,body{width:945px;height:1200px;overflow:hidden}
  body{background:var(--page);font-family:"Montserrat",sans-serif;position:relative}

  .slide{position:absolute;background:var(--paper);container-type:inline-size;overflow:hidden}
  .slide--hero{left:127px;top:67px;width:691px;height:388px}
  .slide--cover-a{left:34px;top:669px;width:425px;height:238px}
  .slide--cover-b{left:473px;top:669px;width:425px;height:238px}
  .slide--content{left:34px;top:922px;width:425px;height:239px}
  .slide--closing{left:473px;top:922px;width:425px;height:239px}

  .banner-shape{position:absolute;inset:0;width:100%;height:100%}

  .brand{position:absolute;color:var(--ink);font-weight:700;line-height:1}
  .brand-name{display:block;font-size:4.7cqw;letter-spacing:.09em}
  .brand-tag{display:block;font-size:1.15cqw;letter-spacing:.42em;margin-top:1.1cqw;padding-left:.3em}
  .slide--cover-a .brand,.slide--cover-b .brand,.slide--hero .brand{left:4.9%;top:8.2%}

  .date{position:absolute;left:70.8%;top:18.6%;display:flex;align-items:center;gap:1.4cqw;
        color:var(--white);font-size:1.2cqw;font-weight:400}
  .date svg{width:2.4cqw;height:2.4cqw}

  .cover-title{position:absolute;left:10.3%;top:36.4%;color:var(--white);font-weight:700;
               font-size:6.1cqw;line-height:1.04;letter-spacing:.005em}
  .cover-subtitle{position:absolute;left:10.3%;top:61.6%;color:var(--white);font-weight:400;font-size:2.1cqw}

  .copyright{position:absolute;font-size:.98cqw;color:var(--muted);font-weight:500;white-space:nowrap}
  .slide--hero .copyright,.slide--cover-a .copyright,.slide--cover-b .copyright{right:4.2%;top:89.3%}

  .content-heading{position:absolute;left:0;right:0;top:7.6%;text-align:center;color:var(--brand-blue);
                   font-size:3.7cqw;font-weight:400;letter-spacing:.03em}
  .content-heading strong{font-weight:700}
  .slide--content .brand{left:2.5%;top:90.6%}
  .slide--content .brand-name{font-size:2.4cqw}
  .slide--content .brand-tag{font-size:.6cqw;margin-top:.4cqw}
  .slide--content .copyright{right:6.6%;top:92.6%;font-size:.9cqw}
  .page-number{position:absolute;right:2.6%;top:91.6%;width:2.4cqw;height:2.4cqw;border-radius:50%;
               background:var(--navy);color:var(--white);font-size:1.1cqw;font-weight:700;
               display:flex;align-items:center;justify-content:center}

  .closing-photo{position:absolute;left:0;top:0;width:100%;height:92.8%;
                 background:linear-gradient(100deg,var(--brand-blue) 0%,#1a73bd 45%,var(--photo-blue) 100%)}
  .slide--closing .brand{left:9.2%;top:32.5%;color:var(--white)}
  .slide--closing .brand-name{font-size:3.6cqw}
  .slide--closing .brand-tag{font-size:.95cqw;margin-top:.7cqw}
  .contact-heading{position:absolute;left:9.2%;top:52.3%;color:var(--white);font-weight:700;font-size:2.3cqw}
  .contact-list{position:absolute;left:9.2%;top:61.8%;list-style:none;color:var(--white);font-size:1.3cqw}
  .contact-list li{display:flex;align-items:center;gap:1.6cqw;height:2.9cqw}
  .contact-list svg{width:2cqw;height:2cqw}
  .slide--closing .copyright{left:0;right:0;top:95%;text-align:center;font-size:.98cqw}
</style>
</head>
<body>

<svg width="0" height="0" style="position:absolute" aria-hidden="true">
  <defs>
    <linearGradient id="field-photo" x1="0" y1="0" x2="1" y2="0.3">
      <stop offset="0" stop-color="#0b6fc2"/>
      <stop offset="0.45" stop-color="#1c72bb"/>
      <stop offset="1" stop-color="#4581b6"/>
    </linearGradient>
    <symbol id="icon-calendar" viewBox="0 0 24 24">
      <rect x="3" y="5" width="18" height="16" rx="2" fill="none" stroke="#fff" stroke-width="1.6"/>
      <line x1="3" y1="10" x2="21" y2="10" stroke="#fff" stroke-width="1.6"/>
      <line x1="8" y1="3" x2="8" y2="7" stroke="#fff" stroke-width="1.6"/>
      <line x1="16" y1="3" x2="16" y2="7" stroke="#fff" stroke-width="1.6"/>
      <g fill="#fff"><rect x="6.5" y="13" width="2.5" height="2"/><rect x="10.8" y="13" width="2.5" height="2"/><rect x="15" y="13" width="2.5" height="2"/><rect x="6.5" y="16.5" width="2.5" height="2"/><rect x="10.8" y="16.5" width="2.5" height="2"/><rect x="15" y="16.5" width="2.5" height="2"/></g>
    </symbol>
  </defs>
</svg>

<!-- Featured cover slide -->
<section class="slide slide--hero">
  <svg class="banner-shape" viewBox="0 0 1249 702" preserveAspectRatio="none">
    <polygon fill="var(--rule-grey)" points="752,182 850,91 1221,91 1221,104 861,104 776,182"/>
    <polygon fill="var(--rule-grey)" points="27,608 376,608 441,566 470,566 392,622 27,622"/>
    <polygon role="img" aria-label="Field photo: engineers in hi-vis gear beside a snowy permafrost cut with an excavator, under a blue overlay"
             fill="url(#field-photo)" points="27,608 376,608 441,566 1221,566 1221,104 861,104 776,182 27,182"/>
  </svg>
  <div class="brand"><span class="brand-name">TUNDRALINE</span><span class="brand-tag">GROUND CONSULTING</span></div>
  <p class="date"><svg><use href="#icon-calendar"/></svg>Friday, June 9, 2023</p>
  <h1 class="cover-title">Expert<br>Permafrost Services</h1>
  <p class="cover-subtitle">Innovative Solutions to Meet Cold Region Challenges</p>
  <p class="copyright">COPYRIGHT © 2022 TUNDRALINE GROUND CONSULTING LLC - ALL RIGHTS RESERVED.</p>
</section>

<!-- Cover slide -->
<section class="slide slide--cover-a">
  <svg class="banner-shape" viewBox="0 0 1249 702" preserveAspectRatio="none">
    <polygon fill="var(--rule-grey)" points="752,182 850,91 1221,91 1221,104 861,104 776,182"/>
    <polygon fill="var(--rule-grey)" points="27,608 376,608 441,566 470,566 392,622 27,622"/>
    <polygon role="img" aria-label="Field photo: engineers beside a snowy permafrost cut, blue overlay"
             fill="url(#field-photo)" points="27,608 376,608 441,566 1221,566 1221,104 861,104 776,182 27,182"/>
  </svg>
  <div class="brand"><span class="brand-name">TUNDRALINE</span><span class="brand-tag">GROUND CONSULTING</span></div>
  <p class="date"><svg><use href="#icon-calendar"/></svg>Friday, June 9, 2023</p>
  <h2 class="cover-title">Expert<br>Permafrost Services</h2>
  <p class="cover-subtitle">Innovative Solutions to Meet Cold Region Challenges</p>
  <p class="copyright">COPYRIGHT © 2022 TUNDRALINE GROUND CONSULTING LLC - ALL RIGHTS RESERVED.</p>
</section>

<!-- Alternate cover slide -->
<section class="slide slide--cover-b">
  <svg class="banner-shape" viewBox="0 0 1249 702" preserveAspectRatio="none">
    <polygon fill="var(--rule-grey)" points="752,182 850,91 1221,91 1221,104 861,104 776,182"/>
    <polygon fill="var(--rule-grey)" points="27,608 376,608 441,566 470,566 392,622 27,622"/>
    <polygon role="img" aria-label="Field photo: layered frozen ground exposed in a snowy cut bank, blue overlay"
             fill="url(#field-photo)" points="27,608 376,608 441,566 1221,566 1221,104 861,104 776,182 27,182"/>
  </svg>
  <div class="brand"><span class="brand-name">TUNDRALINE</span><span class="brand-tag">GROUND CONSULTING</span></div>
  <p class="date"><svg><use href="#icon-calendar"/></svg>Friday, June 9, 2023</p>
  <h2 class="cover-title">Presentation<br>Title Goes Here</h2>
  <p class="cover-subtitle">Sub-Title of Presentation Goes Here</p>
  <p class="copyright">COPYRIGHT © 2022 TUNDRALINE GROUND CONSULTING LLC - ALL RIGHTS RESERVED.</p>
</section>

<!-- Content slide -->
<section class="slide slide--content">
  <h2 class="content-heading"><strong>Heading</strong> Goes Here</h2>
  <div class="brand"><span class="brand-name">TUNDRALINE</span><span class="brand-tag">GROUND CONSULTING</span></div>
  <p class="copyright">COPYRIGHT © 2022 TUNDRALINE GROUND CONSULTING LLC - ALL RIGHTS RESERVED.</p>
  <span class="page-number">3</span>
</section>

<!-- Closing slide -->
<section class="slide slide--closing">
  <div class="closing-photo" role="img" aria-label="Field photo: engineers and an excavator at a snowy permafrost site, blue overlay"></div>
  <div class="brand"><span class="brand-name">TUNDRALINE</span><span class="brand-tag">GROUND CONSULTING</span></div>
  <p class="contact-heading">Contact Us</p>
  <ul class="contact-list">
    <li><svg viewBox="0 0 24 24"><path d="M6.6 3.5l3 3.2-1.8 2.2c1 2.2 2.9 4.2 5.3 5.3l2.2-1.8 3.2 3-1.8 3c-6.9-.3-12.6-6-13-13z" fill="none" stroke="#fff" stroke-width="1.8" stroke-linejoin="round"/></svg>(555) 014-2290</li>
    <li><svg viewBox="0 0 24 24"><circle cx="12" cy="12" r="3.6" fill="none" stroke="#fff" stroke-width="1.8"/><path d="M15.6 9v4.4c0 1.6 2.8 1.9 3.4-.4A7.6 7.6 0 1 0 16 19" fill="none" stroke="#fff" stroke-width="1.8" stroke-linecap="round"/></svg>info@tundralineground.com</li>
    <li><svg viewBox="0 0 24 24"><circle cx="12" cy="12" r="8.5" fill="none" stroke="#fff" stroke-width="1.6"/><ellipse cx="12" cy="12" rx="3.8" ry="8.5" fill="none" stroke="#fff" stroke-width="1.6"/><line x1="3.5" y1="12" x2="20.5" y2="12" stroke="#fff" stroke-width="1.6"/></svg>https://tundralineground.com</li>
  </ul>
  <p class="copyright">COPYRIGHT © 2022 TUNDRALINE GROUND CONSULTING LLC - ALL RIGHTS RESERVED.</p>
</section>

</body>
</html>
```